Business Card Design for Kestrelwood Carpentry

I need a business card design for my carpentry company Kestrelwood Carpentry. Ive attached files with all information I require on both sides. Look forward to seeing your design.

```html
<!DOCTYPE html>
<html lang="en">
<head>
<meta charset="utf-8">
<title>Kestrelwood Carpentry – Business Card</title>
<link href="https://fonts.googleapis.com/css2?family=Archivo+Black&family=Montserrat:wght@400;600&display=swap" rel="stylesheet">
<style>
  :root {
    --orange: #f05a22;
    --ink: #2a2a2a;
    --paper: #f7f7f5;
    --stage: #3a3a3a;
    --cream: #fbe3d4;
    --bullet: #5a2a14;
  }
  * { margin: 0; padding: 0; box-sizing: border-box; }
  html, body { width: 1200px; height: 997px; overflow: hidden; }
  body {
    background: var(--stage);
    display: flex;
    align-items: center;
    justify-content: center;
    gap: 60px;
    font-family: "Montserrat", sans-serif;
  }
  .card {
    width: 520px;
    height: 300px;
    position: relative;
    overflow: hidden;
    box-shadow: 0 14px 30px rgba(0,0,0,.45);
  }

  /* Back side */
  .card-back {
    background: var(--orange);
    color: var(--cream);
    display: flex;
    flex-direction: column;
    align-items: center;
    justify-content: center;
  }
  .back-rule {
    width: 440px;
    height: 3px;
    background: rgba(255,255,255,.16);
  }
  .services {
    list-style: none;
    display: flex;
    flex-direction: column;
    align-items: center;
    gap: 9px;
    margin: 16px 0;
    font-size: 12.5px;
    font-weight: 600;
    letter-spacing: 1.3px;
    line-height: 1.2;
  }
  .services li span + span::before {
    content: "";
    display: inline-block;
    width: 8px; height: 8px;
    border-radius: 50%;
    background: var(--bullet);
    margin: 0 9px 1px;
    vertical-align: middle;
  }
  .back-name {
    margin-top: 14px;
    font-family: "Archivo Black", sans-serif;
    font-size: 13px;
    letter-spacing: 9px;
    padding-left: 9px;
    color: rgba(255,255,255,.28);
  }

  /* Front side */
  .card-front { background: var(--paper); }
  .brand {
    position: absolute;
    top: 40px; left: 30px; right: 30px;
    display: flex;
    flex-direction: column;
    align-items: center;
  }
  .brand-rule {
    align-self: stretch;
    height: 3px;
    background: var(--orange);
  }
  .brand-name {
    margin-top: 12px;
    font-family: "Archivo Black", sans-serif;
    font-size: 40px;
    line-height: 1;
    letter-spacing: 2px;
    color: var(--ink);
  }
  .brand-sub {
    margin-top: 6px;
    font-family: "Archivo Black", sans-serif;
    font-size: 13px;
    line-height: 1;
    letter-spacing: 9px;
    padding-left: 9px;
    color: var(--orange);
  }
  .brand-rule.double-top { margin-top: 10px; }
  .brand-rule.double-bottom { margin-top: 4px; height: 1.5px; }
  .brand-dot {
    position: absolute; top: 69px;
    width: 12px; height: 12px; border-radius: 50%;
    background: var(--orange);
  }
  .brand-dot.left { left: 40px; }
  .brand-dot.right { right: 40px; }

  .contact {
    position: absolute;
    top: 152px; left: 0; right: 0;
    display: flex; flex-direction: column; align-items: center;
  }
  .contact-row { display: flex; align-items: center; gap: 10px; }
  .contact-row .line { width: 80px; height: 1.5px; background: var(--ink); }
  .phone-icon {
    width: 22px; height: 22px; border-radius: 50%;
    background: var(--ink);
    display: flex; align-items: center; justify-content: center;
  }
  .phone-number {
    margin-top: 8px;
    font-weight: 600;
    font-size: 15px;
    color: var(--ink);
    letter-spacing: 1px;
  }
  .pointer {
    position: absolute; left: 50%; bottom: 60px;
    transform: translateX(-50%);
    width: 0; height: 0;
    border-left: 6px solid transparent;
    border-right: 6px solid transparent;
    border-top: 7px solid var(--ink);
  }
  .tagline-band {
    position: absolute; left: 0; right: 0; bottom: 0; height: 52px;
    background: var(--orange);
    display: flex; align-items: center; justify-content: center;
    color: #fff;
    font-size: 15px;
    letter-spacing: 1.5px;
  }
  .tagline-band::before {
    content: ""; position: absolute; top: 6px; left: 0; right: 0;
    height: 2px; background: var(--paper);
  }
  .tagline-band span { margin-top: 8px; }
</style>
</head>
<body>
  <section class="card card-back" aria-label="Card back">
    <div class="back-rule"></div>
    <ul class="services">
      <li><span>DECKS &amp; DESKS</span><span>SHOP FITOUTS</span><span>WALL &amp; ROOF FRAMING</span></li>
      <li><span>REFURBISHMENT</span><span>DOOR &amp; WINDOWS</span><span>FENCES/GATES</span></li>
      <li><span>ATTIC CONVERSIONS</span><span>PRIVACY SCREENS</span><span>TIMBER FLOORING</span></li>
      <li><span>WALL CLADDING</span><span>EXTENSION &amp; MORE...</span></li>
    </ul>
    <div class="back-rule"></div>
    <div class="back-name">KESTRELWOOD CARPENTRY</div>
  </section>

  <section class="card card-front" aria-label="Card front">
    <span class="brand-dot left"></span>
    <span class="brand-dot right"></span>
    <div class="brand">
      <div class="brand-rule"></div>
      <div class="brand-name">KESTRELWOOD</div>
      <div class="brand-sub">CARPENTRY</div>
      <div class="brand-rule double-top"></div>
      <div class="brand-rule double-bottom"></div>
    </div>
    <div class="contact">
      <div class="contact-row">
        <span class="line"></span>
        <span class="phone-icon">
          <svg width="12" height="12" viewBox="0 0 24 24" aria-hidden="true">
            <path fill="#f05a22" d="M6.6 10.8a15.1 15.1 0 0 0 6.6 6.6l2.2-2.2a1 1 0 0 1 1-.25 11.4 11.4 0 0 0 3.6.57 1 1 0 0 1 1 1V20a1 1 0 0 1-1 1A17 17 0 0 1 3 4a1 1 0 0 1 1-1h3.5a1 1 0 0 1 1 1c0 1.25.2 2.45.57 3.57a1 1 0 0 1-.25 1z"/>
          </svg>
        </span>
        <span class="line"></span>
      </div>
      <div class="phone-number">0412 555 208</div>
    </div>
    <div class="pointer"></div>
    <div class="tagline-band"><span>ANYTHING CARPENTRY. ANYWHERE IN SYDNEY</span></div>
  </section>
</body>
</html>
```